依頼詳細
川辺ふれあい会の第7号の会報の原稿を依頼する。この活動を行うボランティア募集案内で①福祉車両、買い物、病院送迎ボランティア募集 ②子ども食堂開催の際のボランティア募集 ③夏季の子ども学習指導、ゲームや遊びボランティア募集 ④高齢者居場所づくりのサロンの話し相手のボランティア募集 ⑤生活支援の一般ボランティア募集(くさとり、清掃、片付けなど)のボランテイア募集の会報の編集依頼

記載項目
デザインを見てから、説明文は後日指示します。
サイズ
A4
ページ数
片面
希望イメージ
シンプル 複雑
単色 カラフル
暗い 明るい
日常 高級
遊び心 厳粛
未来的 伝統的
女性的 男性的
希望する色
青系
納品ファイル
• 高解像度JPG (.jpg)
補足説明
データをいただき、説明文の追加等を加筆し原稿をPDFにして印刷業者へ依頼する。

```html
<!DOCTYPE html>
<html lang="ja">
<head>
<meta charset="utf-8">
<title>川辺ふれあい会 会報第7号</title>
<link rel="stylesheet" href="https://fonts.googleapis.com/css2?family=M+PLUS+Rounded+1c:wght@400;500;700;800&display=swap">
<style>
:root{
  --pink:#e9508f;
  --pink-bg:#f48cb5;
  --navy:#1d3e7a;
  --blue:#2a6bc0;
  --green:#3aa36a;
  --green-soft:#eaf7ee;
  --kid:#e9508f;
  --kid-soft:#fdecf3;
  --study:#6b5bb5;
  --study-soft:#efedfa;
  --salon:#ec8a1f;
  --salon-soft:#fff3e4;
  --daily:#2f7fd0;
  --daily-soft:#e6f1fc;
  --ink:#333;
  --white:#fff;
}
*{box-sizing:border-box;margin:0;padding:0}
html,body{width:846px;height:1200px;overflow:hidden;background:var(--white)}
body{font-family:"M PLUS Rounded 1c",sans-serif;color:var(--ink);position:relative}
.header{position:absolute;left:0;top:0;width:846px;height:262px;background:linear-gradient(180deg,var(--pink-bg),#f6a6c6)}
.title-bar{position:absolute;left:18px;top:12px;width:810px;height:56px;background:var(--white);border-radius:28px;display:flex;align-items:center;justify-content:center;gap:14px}
.title-bar .pre{font-size:26px;font-weight:800;color:var(--navy)}
.title-bar .name{font-size:38px;font-weight:800;color:var(--pink)}
.title-bar .issue{font-size:26px;font-weight:800;color:var(--navy)}
.header-art{position:absolute;left:22px;top:78px;width:600px;height:176px;border-radius:14px;background:linear-gradient(135deg,#fbd3e3,#f9e7ef 55%,#fcd6b8)}
.portrait{position:absolute;left:660px;top:78px;width:96px;height:108px;border:3px solid var(--white);background:linear-gradient(180deg,#c9ccd4,#8d919c)}
.issuer{position:absolute;left:636px;top:192px;width:196px;font-size:10.5px;line-height:1.45;color:var(--white);font-weight:500}
.banner{position:absolute;left:0;top:262px;width:846px;height:56px;background:var(--blue);color:var(--white);font-size:31px;font-weight:800;text-align:center;line-height:56px;letter-spacing:1px}
.card{position:absolute;border:3px solid;border-radius:14px;padding:10px 14px}
.card h2{display:inline-block;font-size:26px;font-weight:800;color:var(--white);padding:0 12px;border-radius:8px;line-height:38px}
.card h2 small{font-size:17px;font-weight:700;margin-left:4px}
.card p{font-size:13px;line-height:1.5;margin-top:6px;font-weight:500}
.card .art{position:absolute;border-radius:10px}
.c-ride{left:26px;top:334px;width:392px;height:188px;border-color:var(--green);background:var(--green-soft)}
.c-ride h2{background:var(--green)}
.c-kid{left:428px;top:334px;width:392px;height:188px;border-color:var(--kid);background:var(--kid-soft)}
.c-kid h2{background:var(--kid)}
.c-study{left:26px;top:534px;width:392px;height:188px;border-color:var(--study);background:var(--study-soft)}
.c-study h2{background:var(--study)}
.c-salon{left:428px;top:534px;width:392px;height:188px;border-color:var(--salon);background:var(--salon-soft)}
.c-salon h2{background:var(--salon)}
.c-daily{left:26px;top:734px;width:794px;height:172px;border-color:var(--daily);background:var(--daily-soft)}
.c-daily h2{background:var(--daily)}
.c-daily p{width:300px}
.contact-band{position:absolute;left:0;top:922px;width:846px;height:30px;background:var(--green);color:var(--white);font-size:15px;font-weight:700;text-align:center;line-height:30px}
.footer{position:absolute;left:0;top:952px;width:846px;height:248px;background:var(--white)}
.mascot{position:absolute;left:22px;top:20px;width:96px;height:120px;border-radius:48px 48px 20px 20px;background:linear-gradient(180deg,#fde3c8,#f5b98a)}
.org{position:absolute;left:132px;top:26px;width:430px;display:flex;align-items:baseline;white-space:nowrap}
.org .kind{font-size:15px;font-weight:700;color:var(--navy)}
.org .name{font-size:34px;font-weight:800;color:var(--blue);line-height:1.1;margin-left:6px}
.phone{position:absolute;left:132px;top:80px;display:flex;align-items:center;gap:10px}
.phone .lead{background:var(--pink);color:var(--white);font-size:15px;font-weight:800;padding:4px 10px;border-radius:6px}
.phone .num{font-size:44px;font-weight:800;color:var(--pink);display:flex;align-items:center;gap:6px}
.hours{position:absolute;left:132px;top:140px;font-size:13px;font-weight:700;color:var(--navy)}
.address{position:absolute;left:22px;top:170px;font-size:10.5px;color:var(--ink)}
.note-box{position:absolute;left:584px;top:18px;width:238px;height:146px;border:2px solid var(--blue);border-radius:10px;padding:12px;font-size:13px;line-height:1.6;color:var(--navy);font-weight:500}
</style>
</head>
<body>
<header class="header">
  <div class="title-bar">
    <span class="pre">NPO法人</span><span class="name">川辺ふれあい会</span><span class="issue">会報第7号</span>
  </div>
  <div class="header-art" role="img" aria-label="ハートの背景に手をつなぐ地域の人々のイラスト"></div>
  <div class="portrait" role="img" aria-label="理事長の顔写真"></div>
  <div class="issuer">2022.2.1発行<br>発行者 理事長 山田○○<br>事務局 佐藤○○<br>TEL 0280-55-3170</div>
</header>

<div class="banner">あなたも参加できるボランティア受付中!</div>

<section class="card c-ride">
  <h2>送迎<small>ボランティア募集</small></h2>
  <p>福祉車両、買い物、病院送迎の<br>ボランティア募集</p>
  <div class="art" style="left:150px;top:92px;width:226px;height:84px;background:linear-gradient(135deg,#cfeedd,#f6f0d8)" role="img" aria-label="車いすの方を福祉車両へ送迎するイラスト"></div>
</section>

<section class="card c-kid">
  <h2>子ども食堂<small>ボランティア募集</small></h2>
  <p>子ども食堂開催の際のボランティア募集</p>
  <div class="art" style="left:150px;top:80px;width:226px;height:96px;background:linear-gradient(135deg,#fcd3e3,#fff0d6)" role="img" aria-label="子どもたちが食卓を囲むイラスト"></div>
</section>

<section class="card c-study">
  <h2>学習<small>ボランティア募集</small></h2>
  <p>夏季の子ども学習指導、ゲームや遊び<br>ボランティア募集</p>
  <div class="art" style="left:150px;top:92px;width:226px;height:84px;background:linear-gradient(135deg,#ddd8f5,#f3eefc)" role="img" aria-label="子どもに勉強を教えるイラスト"></div>
</section>

<section class="card c-salon">
  <h2>サロン<small>ボランティア募集</small></h2>
  <p>高齢者居場所づくりのサロンの話し相手の<br>ボランティア募集</p>
  <div class="art" style="left:150px;top:92px;width:226px;height:84px;background:linear-gradient(135deg,#fde0bd,#fff5e6)" role="img" aria-label="高齢者と談笑するイラスト"></div>
</section>

<section class="card c-daily">
  <h2>日常支援<small>ボランティア募集</small></h2>
  <p>生活支援の一般ボランティア募集<br>(くさとり、清掃、片付けなど)の<br>ボランティア募集</p>
  <div class="art" style="left:340px;top:14px;width:436px;height:140px;background:linear-gradient(135deg,#cfe3f8,#eef6e4)" role="img" aria-label="草取りや清掃、片付けをする人々のイラスト"></div>
</section>

<div class="contact-band">ボランティア参加や手助けのお問い合わせ・お申し込みは</div>

<footer class="footer">
  <div class="mascot" role="img" aria-label="会のマスコットキャラクターのイラスト"></div>
  <div class="org"><span class="kind">特定非営利活動法人</span><span class="name">川辺ふれあい会</span></div>
  <div class="phone">
    <span class="lead">困ったらまず</span>
    <span class="num">
      <svg width="34" height="34" viewBox="0 0 24 24" aria-hidden="true"><path fill="#e9508f" d="M6.6 10.8a15.1 15.1 0 0 0 6.6 6.6l2.2-2.2c.3-.3.7-.4 1-.2 1.1.4 2.3.6 3.6.6.6 0 1 .4 1 1V20c0 .6-.4 1-1 1A17 17 0 0 1 3 4c0-.6.4-1 1-1h3.5c.6 0 1 .4 1 1 0 1.3.2 2.5.6 3.6.1.3 0 .7-.2 1z"/></svg>
      55-3170
    </span>
  </div>
  <div class="hours">※受付時間:午前10時〜12時・午後1時〜3時まで</div>
  <div class="address">〒000-0000 みどり市川辺町1-2-3(川辺地区コミュニティセンター内)</div>
  <div class="note-box">「特定非営利活動法人 川辺ふれあい会」は、地域の困りごとを皆で支え合う会です。お気軽にご相談ください。</div>
</footer>
</body>
</html>
```